Business Card Design Project for Investment Fund

Orvanel Asset Partners is an emerging wealth management firm based in New Jersey. It offers superior investment returns to high net worth individuals and institutions by finding undervalued assets.
We recently selected a company logo which was inspired by the Tucana constellation. Beta Tucanae is a group of six stars, containing star cluster 47 Tucanae, rated the second brightest object in the sky.
Now we need a business card design. Since we are an investment firm, the design should project a sense of stability, growth and professionalism. The owner is interested in something simple yet striking, which of course is consistent with the logo.
Target Market(s)
Wealthy individuals, probably middle aged or older, in the US
Industry/Entity Type
Investment

```html
<!DOCTYPE html>
<html lang="en">
<head>
<meta charset="utf-8">
<title>Orvanel Asset Partners — Business Card</title>
<link href="https://fonts.googleapis.com/css2?family=Tinos&display=swap" rel="stylesheet">
<style>
  :root {
    --card-bg: #ffffff;
    --brand-square: #2c3c9e;
    --brand-ink: #2b3a42;
    --text-ink: #000000;
  }
  html, body {
    margin: 0;
    padding: 0;
    width: 694px;
    height: 1200px;
    overflow: hidden;
    background: var(--card-bg);
  }
  .card {
    position: relative;
    width: 694px;
    height: 1200px;
    background: var(--card-bg);
    font-family: "Tinos", "Times New Roman", serif;
  }
  .brand {
    position: absolute;
    top: 205px;
    left: 0;
    width: 694px;
    text-align: center;
  }
  .brand-square {
    display: block;
    width: 208px;
    height: 208px;
    margin: 0 auto;
  }
  .brand-name {
    margin: 58px 0 0;
    font-size: 46px;
    font-weight: 400;
    color: var(--brand-ink);
    letter-spacing: 1px;
  }
  .contact {
    position: absolute;
    left: 56px;
    top: 812px;
    color: var(--text-ink);
  }
  .contact-name {
    margin: 0 0 14px;
    font-size: 54px;
    font-weight: 400;
    line-height: 62px;
  }
  .contact-details {
    margin: 0;
    font-size: 38px;
    line-height: 49px;
    font-style: normal;
  }
</style>
</head>
<body>
  <main class="card">
    <header class="brand">
      <svg class="brand-square" viewBox="0 0 208 208" aria-hidden="true">
        <rect width="208" height="208" rx="22" fill="var(--brand-square)"/>
      </svg>
      <p class="brand-name">Orvanel Asset Partners</p>
    </header>
    <section class="contact">
      <h1 class="contact-name">Jonah Pellister, CEO</h1>
      <address class="contact-details">
        48 Halden Avenue<br>
        Newark, NJ 07102<br>
        jpellister@orvanelasset.com<br>
        555.318.0274<br>
        www.orvanelasset.com
      </address>
    </section>
  </main>
</body>
</html>
```